Vornique Business Cards

We need new business cards that incorporate our new compnay logo and color scheme. We are a custom publishing company located in Ann Arbor, MI.

Target Market(s)

Deans, Assistant Deans, Executive MBA Program Directors and Faculty at top universities in North America. Top publishers in North America.

Industry/Entity Type

Publishing Company

Requirements
Must have
• The Vornique Logo
The following color palatte:
Gold:
C: 1
M: 6
Y: 25
K: 0

Darker gold
C: 0
M: 31
Y: 100
K: 0

Purple
C: 78
M: 100
Y: 0
K: 33

Teal
C: 87
M: 0
Y: 38
K: 0

Must also be able to fit the following sample b-card information:
www.vornique-example.com
Priya Ostrander
Director, Marketing
2315 Harrow Lane, PO Box 417
Lindenfield, OH 48213-0417
phone: 800-555-0143 x2291
email: postrander@vornique-example.com
Nice to have
• match the look and feel of our website: www.vornique-example.com

```html
<!DOCTYPE html>
<html lang="en">
<head>
<meta charset="utf-8">
<title>Vornique Business Card</title>
<link rel="stylesheet" href="https://fonts.googleapis.com/css2?family=Arimo:wght@700&family=Courier+Prime&family=UnifrakturMaguntia&display=swap">
<style>
  :root {
    --page: #ececec;
    --card: #ffffff;
    --purple: #44207c;
    --gold: #f1c034;
    --gold-dark: #e39f12;
    --teal: #2a9184;
    --ink: #1b1b1b;
  }
  html, body {
    margin: 0;
    width: 1200px;
    height: 900px;
    overflow: hidden;
    background: var(--page);
  }
  .card {
    position: absolute;
    left: 75px;
    top: 150px;
    width: 1050px;
    height: 600px;
    background: var(--card);
    border-radius: 18px;
    overflow: hidden;
    box-shadow: 0 6px 24px rgba(0,0,0,0.12);
  }
  .card__band {
    position: absolute;
    inset: 0;
    clip-path: polygon(0 500px, 780px 0, 1050px 0, 220px 600px, 0 600px);
    background: linear-gradient(135deg, var(--purple) 0%, var(--gold) 45%, var(--teal) 75%, var(--gold) 100%);
    opacity: 0.85;
  }
  .card__name {
    position: absolute;
    left: 300px;
    top: 38px;
    width: 400px;
    text-align: center;
    margin: 0;
    font-family: "UnifrakturMaguntia", serif;
    font-weight: 400;
    font-size: 38px;
    color: var(--gold-dark);
  }
  .card__title {
    position: absolute;
    left: 300px;
    top: 92px;
    width: 400px;
    text-align: center;
    margin: 0;
    font-family: "Arimo", sans-serif;
    font-weight: 700;
    font-size: 19px;
    color: var(--ink);
  }
  .brand {
    position: absolute;
    left: 40px;
    top: 214px;
    display: flex;
    align-items: center;
    gap: 12px;
  }
  .brand__dot {
    width: 22px;
    height: 22px;
    border-radius: 50%;
    background: var(--purple);
  }
  .brand__name {
    font-family: "Arimo", sans-serif;
    font-weight: 700;
    font-size: 46px;
    color: var(--purple);
    line-height: 1;
  }
  .card__contact {
    position: absolute;
    right: 38px;
    top: 330px;
    margin: 0;
    text-align: right;
    font-family: "Courier Prime", monospace;
    font-style: normal;
    font-size: 17px;
    line-height: 1.55;
    color: var(--ink);
  }
</style>
</head>
<body>
  <article class="card">
    <div class="card__band" role="img" aria-label="Decorative diagonal band in the brand's purple, gold and teal"></div>

    <h1 class="card__name">Priya Ostrander</h1>
    <p class="card__title">Director, Marketing</p>

    <div class="brand">
      <span class="brand__dot"></span>
      <span class="brand__name">Vornique</span>
    </div>

    <address class="card__contact">
      www.vornique-example.com<br>
      2315 Harrow Lane, PO Box 417<br>
      Lindenfield, OH 48213-0417<br>
      phone: 800-555-0143 x2291<br>
      email: postrander@vornique-example.com
    </address>
  </article>
</body>
</html>
```